Stationery Design for TAVIQ

I have now selected the logo for my consultancy company. I need some innovative design for my stationary. The audience is senior executives in international banks predominantly in Asia, but also in the Middle East, Africa and Latin America.
My company advises them on solutions to be able to grow their business.

I will update to a vector file in a few hours

Target Market(s)

Senior executives in international Banks.

Industry/Entity Type

Business

Requirements
Should not have
• It should not be forgettable!

```html
<!DOCTYPE html>
<html lang="en">
<head>
<meta charset="utf-8">
<title>TAVIQ Stationery</title>
<link rel="stylesheet" href="https://fonts.googleapis.com/css2?family=Questrial&family=Open+Sans:wght@400;600&display=swap">
<style>
  :root {
    --backdrop: #2a2a2a;
    --paper: #ffffff;
    --paper-soft: #ececec;
    --ink: #5c5c5c;
    --ink-light: #7a7a7a;
    --leaf: #d6e08a;
    --leaf-soft: #eef3c8;
    --teal: #a9d6cf;
    --mark: #c7d873;
  }
  * { box-sizing: border-box; margin: 0; padding: 0; }
  html, body { width: 1200px; height: 900px; overflow: hidden; }
  body {
    background: var(--backdrop);
    font-family: "Open Sans", Arial, sans-serif;
    color: var(--ink);
    position: relative;
  }
  .sheet {
    position: absolute;
    background: var(--paper);
    box-shadow: 0 6px 24px rgba(0,0,0,.5);
    overflow: hidden;
  }
  .wordmark {
    font-family: "Questrial", Arial, sans-serif;
    color: var(--ink);
    letter-spacing: .04em;
    line-height: 1;
    white-space: nowrap;
  }
  .brand-lockup { display: flex; align-items: center; gap: 14px; }
  .brand-dot {
    border-radius: 50%;
    background: var(--mark);
    flex: none;
  }
  .wave-field {
    position: absolute;
    background: linear-gradient(160deg, var(--leaf-soft) 0%, rgba(169,214,207,.45) 45%, rgba(214,224,138,.35) 75%, rgba(255,255,255,0) 100%);
  }

  /* Letterhead */
  .letterhead { left: 70px; top: 139px; width: 440px; height: 622px; }
  .letterhead .wordmark { position: absolute; right: 36px; top: 36px; font-size: 64px; }
  .letterhead .brand-dot { position: absolute; left: 40px; top: 118px; width: 52px; height: 52px; }
  .letterhead .sender {
    position: absolute; left: 40px; top: 184px;
    font-size: 12px; line-height: 1.35; color: var(--ink-light);
  }
  .letterhead .wave-field { right: 0; top: 150px; width: 150px; height: 380px; }

  /* Business cards */
  .card { top: 139px; width: 290px; height: 166px; }
  .card-front { left: 560px; }
  .card-front .wave-field { right: 0; top: 0; width: 110px; height: 166px; }
  .card-front .person { position: absolute; left: 22px; top: 26px; }
  .card-front .person-name { font-family: "Questrial", Arial, sans-serif; font-size: 20px; letter-spacing: .04em; }
  .card-front .person-role { font-size: 10px; color: var(--ink-light); }
  .card-front .contacts { position: absolute; left: 22px; top: 96px; list-style: none; font-size: 9px; color: var(--ink-light); }
  .card-front .contacts li { display: flex; align-items: center; gap: 6px; margin-bottom: 4px; }
  .contact-icon { width: 11px; height: 11px; }

  .card-back { left: 870px; background: linear-gradient(180deg, var(--paper) 0%, var(--paper-soft) 100%); }
  .card-back .brand-lockup { position: absolute; left: 30px; top: 52px; }
  .card-back .brand-dot { width: 56px; height: 56px; }
  .card-back .wordmark { font-size: 40px; }
  .card-back .website { position: absolute; left: 100px; top: 104px; font-size: 10px; color: var(--ink-light); }

  /* Envelope */
  .envelope { left: 560px; top: 461px; width: 600px; height: 300px; background: linear-gradient(180deg, var(--paper) 0%, var(--paper-soft) 100%); }
  .envelope .brand-lockup { position: absolute; left: 34px; top: 34px; }
  .envelope .brand-dot { width: 44px; height: 44px; }
  .envelope .wordmark { font-size: 44px; }
  .envelope .return-address { position: absolute; left: 44px; top: 190px; font-size: 15px; }
  .envelope .window {
    position: absolute; right: 70px; top: 100px; width: 200px; height: 76px;
    background: #d8d8d8; border: 2px solid #3a3a3a; border-radius: 3px;
  }
  .envelope .wave-field { right: 0; top: 0; width: 260px; height: 300px; }
</style>
</head>
<body>

<section class="sheet letterhead">
  <div class="wave-field" role="img" aria-label="Soft green and teal wave decoration"></div>
  <div class="wordmark">TAVIQ</div>
  <div class="brand-dot"></div>
  <p class="sender">address line<br>000 000 000<br>yourmail@com</p>
</section>

<section class="sheet card card-front">
  <div class="wave-field" role="img" aria-label="Soft green and teal wave decoration"></div>
  <div class="person">
    <p class="person-name">YOUR NAME</p>
    <p class="person-role">Company Position</p>
  </div>
  <ul class="contacts">
    <li><svg class="contact-icon" viewBox="0 0 12 12"><circle cx="6" cy="6" r="6" fill="#3a3a3a"/><path d="M4 3.2l1.2 1.6-.6.8c.4.8 1 1.4 1.8 1.8l.8-.6L8.8 8 8 8.9C5.8 8.6 3.4 6.2 3.1 4z" fill="#e3e9a0"/></svg>000 000 000</li>
    <li><svg class="contact-icon" viewBox="0 0 12 12"><circle cx="6" cy="6" r="6" fill="#3a3a3a"/><path d="M6 2.5a2.2 2.2 0 0 1 2.2 2.2C8.2 6.4 6 9.3 6 9.3S3.8 6.4 3.8 4.7A2.2 2.2 0 0 1 6 2.5z" fill="#e3e9a0"/></svg>Your Address</li>
    <li><svg class="contact-icon" viewBox="0 0 12 12"><circle cx="6" cy="6" r="6" fill="#3a3a3a"/><rect x="3" y="4" width="6" height="4.2" fill="#e3e9a0"/><path d="M3 4l3 2.3L9 4" stroke="#3a3a3a" stroke-width=".7" fill="none"/></svg>yourmail@com</li>
  </ul>
</section>

<section class="sheet card card-back">
  <div class="brand-lockup">
    <div class="brand-dot"></div>
    <div class="wordmark">TAVIQ</div>
  </div>
  <p class="website">www.yourwebsite.com</p>
</section>

<section class="sheet envelope">
  <div class="wave-field" role="img" aria-label="Soft green and teal wave decoration"></div>
  <div class="brand-lockup">
    <div class="brand-dot"></div>
    <div class="wordmark">TAVIQ</div>
  </div>
  <div class="window"></div>
  <p class="return-address">Address Line</p>
</section>

</body>
</html>
```